The dental corner of brindlewood web page

website for dental office
Already have domain, mostly information only with address, telephone and google map and hours of operation on top. mobile friendly. SEO a most.

Target Market(s)

Local families

Industry/Entity Type

Dental Clinic

Number of Pages Required

1 page

Font styles to use
Serif

Colors

Designer to choose colors to be used in the design.

Requirements
Must have
• SEO
• Information to find the location
• mobile friendly
• dr's. biography
• services offered
• contect to social media (google, facebook, and instagram)
• Se habla espaƱol
• All insurance accepted
• request an appointment form to notify us

```html
<!DOCTYPE html>
<html lang="en">
<head>
<meta charset="utf-8">
<title>The dental corner of brindlewood</title>
<link href="https://fonts.googleapis.com/css2?family=Montserrat:wght@400;600;700&family=Open+Sans:wght@400;600&display=swap" rel="stylesheet">
<style>
:root{
  --blue:#1f6fb5;
  --blue-dark:#1b3b5c;
  --green:#5cb35c;
  --ink:#4a4f55;
  --muted:#8a9096;
  --band:#eceef1;
  --hero:#f2f3f5;
  --line:#d9dde2;
  --white:#ffffff;
}
*{box-sizing:border-box;margin:0;padding:0}
html,body{width:811px;height:1200px;overflow:hidden;background:var(--white)}
body{position:relative;font-family:"Open Sans",Arial,sans-serif;color:var(--ink)}
.abs{position:absolute}
h2,h3,.nav,.btn{font-family:"Montserrat",Arial,sans-serif}

/* header */
.site-header{left:0;top:0;width:811px;height:32px;background:var(--white)}
.brand{left:58px;top:6px;display:flex;align-items:center;gap:5px;font-family:"Montserrat",sans-serif;font-size:7px;font-weight:600;color:var(--blue)}
.brand-dot{width:14px;height:14px;border-radius:50%;background:var(--blue)}
.nav{left:448px;top:11px;display:flex;gap:14px;font-size:6.5px;color:var(--muted)}
.nav .active{color:var(--blue);font-weight:700}
.topbar{left:600px;top:3px;width:170px;font-size:5px;color:var(--muted);display:flex;gap:8px;justify-content:flex-end;white-space:nowrap}
.topbar b{color:var(--blue-dark);font-weight:600}

/* hero */
.hero{left:0;top:32px;width:811px;height:206px;background:var(--hero)}
.hero-photo{left:470px;top:32px;width:341px;height:206px;background:radial-gradient(ellipse at 62% 45%,#e3cdb9 0%,#ead9ca 40%,rgba(242,243,245,0) 78%)}
.hero-title{left:95px;top:100px;font-size:12px;font-weight:700;color:var(--blue-dark);line-height:1.25}
.hero-title span{color:var(--blue)}
.btn{display:inline-block;background:var(--blue);color:var(--white);font-size:6.5px;font-weight:600;padding:4px 10px;border-radius:2px}
.btn.green{background:var(--green);font-size:5.5px;padding:3px 8px}
.hero-btn{left:95px;top:140px}

/* services */
.panel{background:var(--blue);color:var(--white);padding:10px 10px}
.panel h3{font-size:10px;margin-bottom:5px}
.panel p{font-size:5.2px;line-height:1.45}
.our-services{left:230px;top:248px;width:170px;height:84px}
.who-we-are{left:405px;top:338px;width:167px;height:142px}
.who-we-are .btn{position:absolute;right:10px;bottom:10px;background:var(--green)}
.card{background:var(--white);border:1px solid var(--line);text-align:center;padding-top:8px;width:81px;height:84px}
.card .pic{width:36px;height:36px;border-radius:50%;margin:0 auto 4px;background:linear-gradient(135deg,#e6ddd3,#b9a28c)}
.card h4{font-size:6px;font-weight:600;color:var(--blue-dark);margin-bottom:4px}
.card-a{left:405px;top:248px}
.card-b{left:491px;top:248px}
.card-c{left:230px;top:338px;height:142px;padding-top:30px}
.card-d{left:319px;top:338px;height:142px;padding-top:30px}

/* about */
.about{left:0;top:491px;width:811px;height:217px;background:var(--band)}
.section-title{width:811px;left:0;text-align:center;font-size:11px;font-weight:600;color:var(--blue-dark)}
.section-sub{width:811px;left:0;text-align:center;font-size:5px;color:var(--muted)}
.doctor-photo{left:193px;top:531px;width:84px;height:84px;border-radius:50%;background:linear-gradient(160deg,#dfe4ea,#b9c0c8);border:3px solid var(--white)}
.doctor-name{left:182px;top:627px;width:106px;text-align:center;font-size:5.5px;color:var(--blue-dark)}
.bio{left:302px;top:530px;width:340px;font-size:5.5px;line-height:1.75;text-transform:uppercase;color:var(--muted)}
.bio b{color:var(--blue)}

/* location */
.map{left:230px;top:745px;width:432px;height:174px;background:linear-gradient(135deg,#eef0f1,#e4e9e2);border:1px solid var(--line)}
.map-pin{left:439px;top:816px}
.address{left:230px;top:927px;display:flex;align-items:center;gap:4px;font-size:5.5px;color:var(--muted)}
.address b{color:var(--blue)}
.find-btn{left:609px;top:926px;font-size:5px;padding:3px 6px}

/* contact */
.contact{left:0;top:945px;width:811px;height:210px;background:linear-gradient(180deg,#3a3c3e,#262829)}
.contact .section-title{color:var(--white);top:17px}
.field{background:var(--white);border-radius:2px;height:17px;font-size:5.5px;color:var(--muted);padding:5px 6px}
.f-name{left:238px;top:1004px;width:168px}
.f-phone{left:412px;top:1004px;width:168px}
.f-email{left:238px;top:1027px;width:342px}
.f-msg{left:238px;top:1050px;width:342px;height:58px}
.send-btn{left:527px;top:1116px;background:var(--green);font-size:5.5px}

/* footer */
.site-footer{left:0;top:1155px;width:811px;height:45px;background:var(--white)}
.foot-nav{left:172px;top:1170px;display:flex;gap:12px;font-size:5.5px;color:var(--muted)}
.social{left:574px;top:1169px;display:flex;gap:4px}
.social i{width:7px;height:7px;border-radius:50%;background:var(--muted);display:block}
.copy{left:0;width:811px;top:1186px;text-align:center;font-size:4.5px;color:var(--muted)}
</style>
</head>
<body>

<header class="abs site-header">
  <div class="abs brand"><span class="brand-dot"></span>The dental corner of brindlewood</div>
  <nav class="abs nav"><span class="active">Services</span><span>Resources</span><span>About Us</span><span>Location</span><span>Contact Us</span></nav>
  <div class="abs topbar"><span><b>Hours:</b> Mon–Fri 8am–5pm</span><span><b>Call Now:</b> (555) 014-2290</span></div>
</header>

<section class="abs hero"></section>
<div class="abs hero-photo" role="img" aria-label="Smiling family of parents and a child"></div>
<h2 class="abs hero-title">GET AN APPROPRIATE DENTAL CARE<br><span>JUST IN TIME.</span></h2>
<a class="abs btn hero-btn">Learn More</a>

<div class="abs panel our-services">
  <h3>Our Services</h3>
  <p>Gentle care for every age in one friendly office. We offer checkups, cleanings, fillings, crowns and whitening. All insurance accepted. Se habla español. Call today to book your family visit.</p>
</div>
<div class="abs card card-a"><div class="pic" role="img" aria-label="Dentist with patient"></div><h4>Primary care</h4><span class="btn green">Learn more</span></div>
<div class="abs card card-b"><div class="pic" role="img" aria-label="Dental therapy session"></div><h4>Therapy</h4><span class="btn green">Learn more</span></div>
<div class="abs card card-c"><div class="pic" role="img" aria-label="Dental implant model"></div><h4>Implantations</h4><span class="btn green">Learn more</span></div>
<div class="abs card card-d"><div class="pic" role="img" aria-label="Payment and insurance help"></div><h4>Financial help</h4><span class="btn green">Learn more</span></div>
<div class="abs panel who-we-are">
  <h3>Who we are</h3>
  <p>A local family practice serving Brindlewood for years. Our caring team keeps every visit calm, clear and comfortable.</p>
  <span class="btn">Learn more</span>
</div>

<section class="abs about"></section>
<h2 class="abs section-title" style="top:500px">About Us.</h2>
<div class="abs section-sub" style="top:515px">Doctor</div>
<div class="abs doctor-photo" role="img" aria-label="Portrait of the dentist"></div>
<div class="abs doctor-name">Helena Marsh, Dentist</div>
<p class="abs bio"><b>Dr. Helena Marsh</b> has cared for local families for over fifteen years. She studied dentistry at state university and trained in implant and gentle family care. <b>She speaks Spanish</b> and welcomes patients of every age. Her office accepts all insurance plans and makes each visit easy, calm and clear. Outside the clinic she enjoys time with her children and volunteers at free school checkup days across Brindlewood. <b>Book a visit</b> and meet her friendly team.</p>

<h2 class="abs section-title" style="top:722px">Find Us.</h2>
<div class="abs map" role="img" aria-label="Street map showing the office location"></div>
<svg class="abs map-pin" width="12" height="16" viewBox="0 0 10 14"><path d="M5 0a5 5 0 0 0-5 5c0 3.5 5 9 5 9s5-5.5 5-9a5 5 0 0 0-5-5zm0 7a2 2 0 1 1 0-4 2 2 0 0 1 0 4z" fill="#1f6fb5"/></svg>
<div class="abs address">
  <svg width="8" height="8" viewBox="0 0 10 10"><path d="M5 0a3.5 3.5 0 0 0-3.5 3.5C1.5 6 5 10 5 10s3.5-4 3.5-6.5A3.5 3.5 0 0 0 5 0zm0 5a1.4 1.4 0 1 1 0-2.8A1.4 1.4 0 0 1 5 5z" fill="#5cb35c"/></svg>
  <b>Our Location:</b> 48 Larkspur Avenue, Brindlewood
</div>
<a class="abs btn find-btn">How to Find Us</a>

<section class="abs contact">
  <h2 class="section-title abs">Get In Touch.</h2>
</section>
<div class="abs field f-name">Name</div>
<div class="abs field f-phone">Phone</div>
<div class="abs field f-email">Email</div>
<div class="abs field f-msg">Your message</div>
<a class="abs btn send-btn">Contact Us</a>

<footer class="abs site-footer"></footer>
<nav class="abs foot-nav"><span>Services</span><span>Resources</span><span>About Us</span><span>Location</span><span>Contact Us</span></nav>
<div class="abs social"><i></i><i></i><i></i></div>
<div class="abs copy">© 2024 The dental corner of brindlewood. All rights reserved.</div>

</body>
</html>
```